Web application design for investigative software

ThreadKove is an investigation web application that would organize, create visualizations and allow collaboration. It’s available to anyone and can be used by students, historians, watchdog groups, civic hackers, investigative reporters, mystery enthusiasts, authors, even conspiracy theorists.

We are looking for two related pages. The first, a splash, or front, page and the second a ‘template’ for the web application. They should both be styled the same. The only restriction is that the logo is set.

The design should also be modern and visually well organized — employing a combination of visual devices and info graphics. Keep it light and not too heavy but strong/ professional. Do not be influenced by the current colors of threadkove.example, though the colors should be compatible with the logo..

The pages should be compatible with bootstrap, mostly for it’s JS and component functionality. It can be advised by the designer that a subset of bootstrap be used.

The splash page.
Something along the lines of (though not a copy of) :
https://www.brimloft.example/advertise
http://www.palvornhosting.example/
http://www.murkelsoft.example/
http://www.vontasky.example/

I have a very rough wire frame ish html file uploaded. Use a a guide, but alternate ideas are encouraged.

The application page should have some sort of bar for at the top for system level links a header and a footer. A vertical column to the left between the header and footer for ads, though this will be dynamic as a user can pay out of seeing adds. All dynamic actions will be made by the developers at ThreadKove.

WARNING. Please do not submit pre-made templates from some template website. We can do that ourselves for free.

This project will deliver CODE. HTML, CSS and supporting graphics and files.

```html
<!DOCTYPE html>
<html lang="en">
<head>
<meta charset="utf-8">
<title>ThreadKove – Area Application</title>
<link rel="stylesheet" href="https://fonts.googleapis.com/css2?family=Mulish:wght@300;400;700;800&display=swap">
<style>
:root{
  --red:#d42a1a;
  --red-text:#c9150b;
  --blue:#0aaef0;
  --ink:#3b3b3b;
  --body:#5e5e5e;
  --page:#eef0f2;
  --header:#f0f2f4;
  --line:#dcdcdc;
  --footer:#454545;
}
*{box-sizing:border-box;margin:0;padding:0}
html,body{width:1200px;height:1109px;overflow:hidden}
body{background:var(--page);font-family:"Mulish",sans-serif;color:var(--body);position:relative}
.top-bar{position:absolute;left:0;top:0;width:1200px;height:4px;background:var(--red)}
.site-header{position:absolute;left:0;top:4px;width:1200px;height:77px;background:var(--header);border-bottom:1px solid #d8d8d8}
.brand{position:absolute;left:168px;top:16px;display:flex;align-items:center;gap:8px}
.brand-mark{width:40px;height:40px;border-radius:50%;background:var(--red)}
.brand-name{font-size:23px;font-weight:700;color:var(--ink);line-height:1}
.brand-tag{font-size:7px;color:var(--ink);margin-top:3px;display:block;font-weight:400}
.main-nav{position:absolute;left:544px;top:24px;display:flex;align-items:center}
.main-nav a{font-size:12px;color:var(--ink);text-decoration:none;letter-spacing:.3px;padding:0 15px;height:34px;line-height:34px}
.main-nav a.active{background:#fff;border:1px solid #d6d6d6;border-radius:2px;padding:0 18px}
.main-nav .sep{width:1px;height:22px;background:#d6d6d6}
.btn{position:absolute;top:22px;height:38px;line-height:38px;text-align:center;color:#fff;font-weight:700;font-size:14px;text-decoration:none}
.btn-login{left:839px;width:81px;background:var(--blue)}
.btn-register{left:926px;width:108px;background:var(--red)}
.hero{position:absolute;left:0;top:81px;width:1200px;height:201px;background:linear-gradient(90deg,#2b4a6a 0%,#8a6a52 25%,#c58a4c 50%,#c99a6c 75%,#8f9fb4 100%)}
.hero-shade{position:absolute;inset:0;background:linear-gradient(160deg,rgba(0,0,0,.1) 0%,rgba(0,0,0,0) 60%,rgba(255,255,255,.35) 100%)}
.hero-figure{position:absolute;left:765px;top:14px;width:200px;height:175px;border-radius:40% 40% 20% 20%;background:linear-gradient(180deg,#e9e9e9,#bdbdbd)}
.hero-title{position:absolute;left:246px;top:73px;font-size:37px;color:#fff;font-weight:300}
.hero-title strong{font-weight:800}
.ad-column{position:absolute;left:165px;top:333px;width:255px;height:510px;border:2px solid #dedede;background:#f4f4f4}
.ad-slot{position:absolute;inset:0;background:linear-gradient(180deg,#fbfbfb 0%,#f1e6da 45%,#ebebeb 100%)}
.content{position:absolute;left:468px;top:330px;width:567px}
.section-title{font-size:27px;font-weight:300;color:var(--red-text);letter-spacing:.3px}
.section-title strong{color:var(--ink);font-weight:700}
.intro-box{margin-top:17px;background:#fff;border:1px solid #e2e2e2;padding:16px 22px 0;height:209px}
.intro-box p{font-size:14.4px;line-height:18px;font-weight:300;color:var(--body)}
.intro-box p+p{margin-top:18px}
.intro-box b{color:var(--red-text);font-weight:700}
.variations{margin-top:27px}
.variations .lead{margin-top:10px;font-size:14.4px;line-height:18px;font-weight:300;padding-bottom:16px;border-bottom:1px solid var(--line)}
.story{display:flex;gap:21px;padding:18px 0 17px 1px;border-bottom:1px solid var(--line)}
.story:last-child{border-bottom:0}
.story-photo{width:87px;height:88px;flex:none}
.story p{font-size:14.4px;line-height:18px;font-weight:300}
.read-more{display:inline-block;margin-top:4px;font-size:14px;color:var(--red-text);text-decoration:none;font-weight:400}
.read-more strong{color:var(--ink);font-weight:700}
.site-footer{position:absolute;left:0;top:1031px;width:1200px;height:78px;background:var(--footer)}
.copyright{position:absolute;left:165px;top:31px;font-size:12px;color:#eee}
.to-top{position:absolute;left:578px;top:17px;width:44px;height:44px;border-radius:50%;background:#5e5e5e;display:flex;align-items:center;justify-content:center}
.to-top span{width:26px;height:26px;border-radius:50%;background:#e8482c;display:flex;align-items:center;justify-content:center}
.social{position:absolute;left:903px;top:25px;display:flex;gap:8px}
.social a{width:27px;height:27px;border-radius:50%;border:2px solid #f2f2f2;display:block}
</style>
</head>
<body>
<div class="top-bar"></div>
<header class="site-header">
  <div class="brand"><span class="brand-mark"></span><div><span class="brand-name">ThreadKove</span><span class="brand-tag">Track, Relate, Investigate, Solve!</span></div></div>
  <nav class="main-nav"><a class="active" href="#">HOME</a><a href="#">ABOUT US</a><span class="sep"></span><a href="#">CONTACT US</a></nav>
  <a class="btn btn-login" href="#">LOGIN</a>
  <a class="btn btn-register" href="#">REGISTER</a>
</header>

<section class="hero">
  <div class="hero-shade" role="img" aria-label="Blurred office background photograph"></div>
  <div class="hero-figure" role="img" aria-label="White 3D figure searching with a magnifying glass"></div>
  <h1 class="hero-title">Area <strong>Application</strong></h1>
</section>

<aside class="ad-column">
  <div class="ad-slot" role="img" aria-label="Sponsored advertisement banner"></div>
</aside>

<main class="content">
  <h2 class="section-title">Area <strong>Application</strong></h2>
  <div class="intro-box">
    <p>There are <b>many variations</b> of passages of Lorem Ipsum <b>available,</b> but the majority have <b>suffered alteration</b> in some form, by injected humour, or randomised words which don't look even <b>slightly believable</b>. If you are going to use a <b>passage</b> of Lorem Ipsum,</p>
    <p>you need to be sure there isn't anything embarrassing hidden in the middle of text. All the Lorem Ipsum generators on the Internet tend to repeat predefined chunks as necessary, making this the first true generator on the Internet. It uses a dictionary of over 200 Latin words,</p>
  </div>
  <div class="variations">
    <h2 class="section-title">There are <strong>Many Variations</strong></h2>
    <p class="lead">There are many variations of passages of Lorem Ipsum available, but the majority have suffered alteration in some form, by injected humour, or randomised words which don't look even slightly believable. If you are going to use a passage of Lorem Ipsum, you need to be sure there isn't anything..</p>
    <article class="story">
      <div class="story-photo" role="img" aria-label="Portrait photo of a man in a dark suit" style="background:linear-gradient(180deg,#3a3a3a,#1a1a1a)"></div>
      <div><p>There are many variations of passages of Lorem Ipsum available, but the majority have suffered alteration in some form, by injected humour, or randomised words which don't look even slightly believable. If you are going to use a passage.</p><a class="read-more" href="#">Read <strong>More</strong> ›</a></div>
    </article>
    <article class="story">
      <div class="story-photo" role="img" aria-label="Portrait photo of a smiling blonde woman" style="background:linear-gradient(180deg,#e2cf9e,#b08a5c)"></div>
      <div><p>There are many variations of passages of Lorem Ipsum available, but the majority have suffered alteration in some form, by injected humour, or randomised words which don't look even slightly believable. If you are going to use a passage.</p><a class="read-more" href="#">Read <strong>More</strong> ›</a></div>
    </article>
  </div>
</main>

<footer class="site-footer">
  <p class="copyright">Copyright 2014, ThreadKove Inc.</p>
  <a class="to-top" href="#" aria-label="Back to top"><span><svg width="14" height="10" viewBox="0 0 14 10"><path d="M2 8 L7 3 L12 8" fill="none" stroke="#fff" stroke-width="3" stroke-linecap="round"/></svg></span></a>
  <div class="social"><a href="#" aria-label="Social link 1"></a><a href="#" aria-label="Social link 2"></a><a href="#" aria-label="Social link 3"></a><a href="#" aria-label="Social link 4"></a></div>
</footer>
</body>
</html>
```